Window Treatment business needs website redesigned.

We need a revamp and refresh of our current site www.velmorin.ca
Looking to attract very high end customer. It should be a very simple design with very little text. This site will be visited by prospective homeowners, designers, builders and architects. They should feel that they are dealing with a high-end product selection, where experience, customer service and unique product offering is the focus. The content will be to highlight our services and highlight the manufacturers we sell, using a few rich photos to highlight the products. We should NOT look like we are a very large company. It should NOT have discounts/savings buttons and many menus to choose from. We offer over 15 years experience to narrow the many market options, to provide the right technical solution.
We specialize in products that are not readily available on the market and specifically motorized systems for indoors and outdoors.
Our main suppliers are Quarnel.com, Dexavo.com
We carry our own locally manufactured product line of roller shades.
Main product pictures should be of roller shades, outdoor bug screens, awnings and outdoor pergolas.

Reason: I understand that Christmas is coming up real short and many people are extremely busy. If you have a CREATIVE gifting you still want to submit, I look forward to your idea!

Reason: Due to holiday season, we have not had sufficient time to review to make a final decision. Thank you for your patience!

Target Market(s)

High end home owners, designers, builders, architects

Industry/Entity Type

Contractor

Coding

Coded - Design and coding required

Number of Pages Required

3 page

Font styles to use
Sans Serif

Requirements
Must have
• Landing page with full size image like homepage of borvela.it
• Products page that highlights products with simple product shot image, description and link to manufacturer.
• On main page a scrolling of customer reviews.
• I want a very simple, eye-catching, emotional image for homepage. It does not need to include any product image.
• An image that shows technology combining/meshing with hand craftsmanship.
• Focus is on design.
• http://www.borvela.it/en/gallery is a great layout and design.
Nice to have
• Logo shape for icons and watermark should be used.
• Look like and have simple motion effects like tirquel.com or manvexo.com
Should not have
• Generic/standard looking feel like gostrel.com or plinkwardcove.ca
• No use of green as background only subtle text.
• Lots of text and pages.

```html
<!DOCTYPE html>
<html lang="en">
<head>
<meta charset="utf-8">
<title>Velmorin – Window Treatment Solutions</title>
<link href="https://fonts.googleapis.com/css2?family=Jost:wght@400;500;700&family=Lora:ital@1&display=swap" rel="stylesheet">
<style>
  :root{
    --green:#6db33f;
    --white:#ffffff;
    --soft:#e6e8e6;
    --muted:#c9ceca;
    --octagon:#eeeeee;
    --ink:#1f2421;
  }
  *{margin:0;padding:0;box-sizing:border-box}
  html,body{width:1200px;height:643px;overflow:hidden;background:#2b3330}
  body{font-family:"Jost",sans-serif;color:var(--white);position:relative}
  .hero-photo{position:absolute;inset:0;
    background:
      linear-gradient(180deg,rgba(20,26,24,.35) 0%,rgba(20,26,24,.15) 50%,rgba(16,22,22,.55) 100%),
      linear-gradient(120deg,#5d5f55 0%,#4a4d44 25%,#3a4a48 45%,#5f7a80 62%,#4f6a60 78%,#2f3a34 100%);}
  .screen-shade{position:absolute;left:95px;top:160px;width:575px;height:320px;background:rgba(30,30,28,.35)}

  .brand{position:absolute;left:132px;top:27px;display:flex;align-items:center;gap:8px}
  .brand-mark{width:50px;height:50px;border:3px solid var(--white);border-radius:50%}
  .brand-name{font-size:30px;font-weight:400;letter-spacing:.5px;line-height:1}
  .brand-tag{font-size:12px;margin-top:3px;line-height:1}

  .util-links{position:absolute;right:132px;top:27px;font-size:10.5px;letter-spacing:.2px;display:flex;gap:7px}
  .util-links span.sep{opacity:.9}

  .main-nav{position:absolute;top:63px;left:727px;display:flex;align-items:center;font-size:12.5px;letter-spacing:.4px}
  .main-nav a{color:var(--white);text-decoration:none}
  .main-nav .active{background:var(--green);width:66px;height:30px;display:flex;align-items:center;justify-content:center}
  .main-nav .gallery{margin-left:47px}
  .main-nav .contact{margin-left:58px}
  .main-nav .search{margin-left:56px;display:flex}

  .slide-arrow{position:absolute;top:338px}
  .slide-arrow.prev{left:78px}
  .slide-arrow.next{left:1100px}

  .headline{position:absolute;left:132px;top:258px;font-size:35px;letter-spacing:1px;line-height:1;font-weight:400}
  .headline strong{font-weight:700}
  .subline{position:absolute;left:132px;top:307px;font-size:14.5px;letter-spacing:.3px;color:var(--soft)}
  .divider{position:absolute;left:132px;top:345px;width:148px;height:1px;background:var(--white)}
  .divider-dash{position:absolute;left:284px;top:345px;width:22px;border-top:1px dashed var(--white)}

  .review{position:absolute;left:132px;top:392px;width:440px;height:70px}
  .review-photo{position:absolute;left:0;top:0;width:50px;height:50px;border-radius:50%;background:linear-gradient(160deg,#d9d6d2,#b9aa9c);border:2px solid var(--white)}
  .review-text{position:absolute;left:63px;top:-4px;font-family:"Lora",serif;font-style:italic;font-size:12.5px;line-height:24px;color:var(--white);width:420px;text-indent:22px}
  .quote-mark{position:absolute;font-family:"Lora",serif;font-style:italic;font-size:26px;color:var(--muted);line-height:1}
  .quote-mark.open{left:63px;top:-6px}
  .quote-mark.close{left:350px;top:40px}
  .review-name{position:absolute;left:63px;top:52px;font-size:11px;font-weight:700;color:var(--green);letter-spacing:.3px}
  .review-controls{position:absolute;left:396px;top:50px;display:flex;gap:6px}
  .review-controls span{width:17px;height:16px;border:1px solid var(--muted);display:flex;align-items:center;justify-content:center}

  .service-map{position:absolute;left:700px;top:180px}

  .footer{position:absolute;left:132px;right:58px;top:588px;display:flex;align-items:center;font-size:9.5px;letter-spacing:.3px;color:var(--muted)}
  .footer-mark{width:22px;height:22px;border:2px solid var(--muted);border-radius:50%;margin-right:8px}
  .connect{margin-left:auto;display:flex;align-items:center;gap:0}
  .social{display:flex;gap:22px;margin-left:14px}
  .social span{width:10px;height:10px;border-radius:50%;background:var(--muted)}
  .slide-code{margin-left:72px;font-size:11px}
</style>
</head>
<body>
  <div class="hero-photo" role="img" aria-label="Patio under a retractable awning with a lowered motorized bug screen, lake and mountains beyond"></div>
  <div class="screen-shade" aria-hidden="true"></div>

  <header>
    <div class="brand">
      <div class="brand-mark" aria-hidden="true"></div>
      <div>
        <div class="brand-name">Velmorin</div>
        <div class="brand-tag">Window Treatment Solutions</div>
      </div>
    </div>

    <nav class="util-links">
      <span>LANGUAGES</span><span class="sep">|</span>
      <span>NEWSLETTER</span><span class="sep">|</span>
      <span>COPYRIGHTS</span><span class="sep">|</span>
      <span>PLAZABOOK</span><span class="sep">|</span>
      <span>PICTORAMA</span><span class="sep">|</span>
      <span>VIDSTREAM</span>
    </nav>

    <nav class="main-nav">
      <a class="active" href="#">HOME</a>
      <a class="gallery" href="#">GALLERY</a>
      <a class="contact" href="#">CONTACT</a>
      <span class="search" aria-label="Search">
        <svg width="11" height="11" viewBox="0 0 11 11"><circle cx="4.5" cy="4.5" r="3.3" fill="none" stroke="#fff" stroke-width="1.8"/><line x1="7" y1="7" x2="10" y2="10" stroke="#fff" stroke-width="2"/></svg>
      </span>
    </nav>
  </header>

  <svg class="slide-arrow prev" width="22" height="68" viewBox="0 0 22 68"><polyline points="21,1 1,34 21,67" fill="none" stroke="#fff" stroke-width="1"/></svg>
  <svg class="slide-arrow next" width="22" height="68" viewBox="0 0 22 68"><polyline points="1,1 21,34 1,67" fill="none" stroke="#fff" stroke-width="1"/></svg>

  <main>
    <h1 class="headline"><strong>MOTORIZED</strong> BUG SCREEN</h1>
    <p class="subline">Instantly transform an open patio into a bug free zone.</p>
    <div class="divider"></div><div class="divider-dash"></div>

    <section class="review">
      <div class="review-photo" role="img" aria-label="Customer portrait"></div>
      <span class="quote-mark open">“</span>
      <p class="review-text">Neque porro quisquam est, qui dolorem ipsum quia dolor sit amet, consectetur, adipisci velit, quia non numquam eius...</p>
      <span class="quote-mark close">”</span>
      <p class="review-name">-MARTIN ALDOUS</p>
      <div class="review-controls">
        <span><svg width="6" height="8" viewBox="0 0 6 8"><polyline points="5,1 1,4 5,7" fill="none" stroke="#fff"/></svg></span>
        <span><svg width="6" height="8" viewBox="0 0 6 8"><polyline points="1,1 5,4 1,7" fill="none" stroke="#fff"/></svg></span>
      </div>
    </section>

    <svg class="service-map" width="400" height="370" viewBox="0 0 400 370" font-family="Jost, sans-serif">
      <defs>
        <marker id="arrowhead" viewBox="0 0 10 10" refX="5" refY="5" markerWidth="7" markerHeight="7" orient="auto">
          <path d="M0,0 L10,5 L0,10 L3,5 Z" fill="#e6e8e6"/>
        </marker>
        <polygon id="octagon" points="-23,-56 23,-56 56,-23 56,23 23,56 -23,56 -56,23 -56,-23"/>
      </defs>

      <g fill="none" stroke="#e6e8e6" stroke-width="2" stroke-dasharray="1.5 3" stroke-linecap="round" marker-end="url(#arrowhead)">
        <path d="M66 125 Q58 62 126 58"/>
        <path d="M256 58 Q312 58 313 124"/>
        <path d="M313 242 Q314 305 254 310"/>
        <path d="M128 312 Q66 314 68 246"/>
      </g>

      <g class="octagon-card" transform="translate(191,63)">
        <use href="#octagon" fill="#eeeeee" stroke="#6db33f" stroke-width="2.5"/>
        <g fill="#6db33f">
          <circle cx="-6" cy="-16" r="8"/><circle cx="-6" cy="-16" r="3" fill="#eeeeee"/>
          <circle cx="8" cy="-22" r="5"/><circle cx="8" cy="-10" r="5"/>
        </g>
        <text y="22" text-anchor="middle" font-size="11.5" fill="#1f2421">NEQUE PORR</text>
      </g>

      <g class="octagon-card" transform="translate(71,183)">
        <use href="#octagon" fill="#eeeeee" stroke="#6db33f" stroke-width="2.5"/>
        <rect x="-18" y="-29" width="36" height="28" rx="3" fill="#6db33f"/>
        <rect x="-7" y="-34" width="14" height="6" rx="1" fill="none" stroke="#6db33f" stroke-width="2.5"/>
        <path d="M-2,-22 h4 v5 h5 v4 h-5 v5 h-4 v-5 h-5 v-4 h5z" fill="#eeeeee"/>
        <text y="22" text-anchor="middle" font-size="11.5" fill="#1f2421">NEQUE PORR</text>
      </g>

      <g class="octagon-card" transform="translate(191,183)">
        <use href="#octagon" fill="#6db33f" stroke="#eeeeee" stroke-width="2.5"/>
        <path d="M-19,-16 L0,-33 L19,-16 M-13,-18 V0 H-4 V-10 H4 V0 H13 V-18" fill="none" stroke="#fff" stroke-width="4" stroke-linejoin="round"/>
        <text y="22" text-anchor="middle" font-size="11.5" fill="#ffffff">NEQUE PORR</text>
      </g>

      <g class="octagon-card" transform="translate(311,183)">
        <use href="#octagon" fill="#eeeeee" stroke="#6db33f" stroke-width="2.5"/>
        <rect x="-18" y="-20" width="8" height="20" rx="1" fill="#6db33f"/>
        <path d="M-7,-20 L-1,-34 Q4,-36 4,-30 L2,-22 H14 Q18,-21 17,-16 L14,-2 Q13,0 10,0 H-7 Z" fill="#6db33f"/>
        <text y="22" text-anchor="middle" font-size="11.5" fill="#1f2421">NEQUE PORR</text>
      </g>

      <g class="octagon-card" transform="translate(191,303)">
        <use href="#octagon" fill="#eeeeee" stroke="#6db33f" stroke-width="2.5"/>
        <circle cy="-17" r="15" fill="none" stroke="#6db33f" stroke-width="6"/>
        <circle cy="-17" r="7" fill="none" stroke="#6db33f" stroke-width="2"/>
        <g stroke="#eeeeee" stroke-width="3"><line x1="-11" y1="-28" x2="-7" y2="-24"/><line x1="11" y1="-28" x2="7" y2="-24"/><line x1="-11" y1="-6" x2="-7" y2="-10"/><line x1="11" y1="-6" x2="7" y2="-10"/></g>
        <text y="22" text-anchor="middle" font-size="11.5" fill="#1f2421">NEQUE PORR</text>
      </g>
    </svg>
  </main>

  <footer class="footer">
    <div class="footer-mark" aria-hidden="true"></div>
    <span>COPYRIGHTS © 2016 . VELMORIN | ALLRIGHTS RESERVED.</span>
    <div class="connect">
      <span>CONNECT WITH US :</span>
      <div class="social" aria-label="Social links"><span></span><span></span><span></span><span></span><span></span></div>
      <span class="slide-code">C11</span>
    </div>
  </footer>
</body>
</html>
```